Need 2 sided card for Loomfield Goods Co. Logo supplied.

I am looking for a business card for my online craft supply business.

I have a very simple design already which I am kind of happy with (see attached pdf) - but would like suggestions for something a little more creative. Design MUST be clean. Super clean! Think thin lines and not blocks of color...

Design must be clean and crisp. No other colors other than in palette (see link below)

I would also like to possible incorporate my tagline - maybe on the front but definitely on the back:
"HollowReed Ideas & Hobby Materials"

Logo file is supplied, but I think spacing on the card may required the wording to be moved underneaths the camera icon - which is fine. Font in logo is Maven Pro. OPEN TO USE OF OTHER FONTS ON CARD BUT MUST BE CLEAN DESIGN.

FRONT OF CARD
All information on attached pdf is correct and should be shown in your design.

BACK OF CARD
Needs to show www.tindalerow.example and maybe logo repeat and tagline.

SIZE
New Zealand sized - meaning finished card will be 90 x 55mm
Printing requirements: printed area is 90mm x 55mm with a 2mm bleed all round.

COLORS
Color palette used in logo can be seen here for HEX and RGB reference: http://www.huebankly.example/palette/8627410/website

NOTE: PAYMENT WILL BE MADE FOR THE BEST DESIGN - EVEN IF I DECIDE NOT TO USE IT.
Updates

Thank you all so much for your designs. I will be providing feedback to ALL designers tomorrow. This weekend is a holiday weekend here in New Zealand and so no work for a few days. Thank-you again - I appreciate your time and creativity!

Industry/Entity Type

Camera

Font styles to use
Other font styles liked:
• Maven Pro - open to others

Requirements
Must have
• Clean design. Logo must be prominent for brand recognition. All contact information must be shown.
Nice to have
• Tagline - at least on reverse

```html
<!DOCTYPE html>
<html lang="en">
<head>
<meta charset="utf-8">
<title>Loomfield Goods Co. – Business Card</title>
<link rel="stylesheet" href="https://fonts.googleapis.com/css2?family=Maven+Pro:wght@400;500;700&display=swap">
<style>
  :root {
    --orange: #f26a3d;
    --lime: #c9c11f;
    --charcoal: #58585a;
    --text-grey: #6a6a6c;
    --teal: #3fb3a6;
    --card: #ffffff;
    --backdrop: #4e3626;
  }
  * { margin: 0; padding: 0; box-sizing: border-box; }
  html, body {
    width: 1200px; height: 418px; overflow: hidden;
    background: var(--backdrop);
    font-family: "Maven Pro", sans-serif;
  }
  .canvas { position: relative; width: 1200px; height: 418px; }
  .card {
    position: absolute; width: 470px; height: 286px;
    background: var(--card); overflow: hidden;
    box-shadow: 0 4px 12px rgba(0,0,0,.35);
  }
  .card--front { left: 120px; top: 70px; }
  .card--back { left: 619px; top: 72px; }
  .card__waves { position: absolute; inset: 0; width: 470px; height: 286px; }

  .tagline--banner {
    position: absolute; left: 20px; top: 14px;
    color: #fff; font-weight: 700; font-size: 17px; line-height: 24px;
  }
  .holder-name {
    position: absolute; left: 252px; top: 100px;
    color: var(--charcoal); font-weight: 700; font-size: 24px; letter-spacing: .5px;
  }
  .contact-list {
    position: absolute; left: 252px; top: 176px; list-style: none;
  }
  .contact-list li {
    display: flex; align-items: center; gap: 6px;
    height: 15.6px; font-size: 12.5px; color: var(--text-grey);
  }
  .contact-list .dot { width: 10px; height: 10px; border-radius: 50%; flex: none; }
  .dot--orange { background: var(--orange); }
  .dot--lime { background: var(--lime); }
  .dot--grey { background: var(--charcoal); }
  .dot--teal { background: var(--teal); }

  .brand { position: absolute; display: flex; flex-direction: column; align-items: center; }
  .brand__mark { border-radius: 50%; background: var(--orange); }
  .brand__name { color: var(--charcoal); font-weight: 400; white-space: nowrap; }
  .brand--front { left: 18px; top: 158px; width: 200px; }
  .brand--front .brand__mark { width: 50px; height: 50px; margin-bottom: 10px; }
  .brand--front .brand__name { font-size: 24px; }
  .brand--back { left: 0; top: 44px; width: 470px; }
  .brand--back .brand__mark { width: 66px; height: 66px; margin-bottom: 10px; }
  .brand--back .brand__name { font-size: 38px; }
  .tagline--back {
    position: absolute; left: 0; top: 181px; width: 470px; text-align: center;
    color: var(--text-grey); font-size: 17px; letter-spacing: .3px;
  }
</style>
</head>
<body>
<main class="canvas">
  <section class="card card--front" aria-label="Card front">
    <svg class="card__waves" viewBox="0 0 470 286" aria-hidden="true">
      <path d="M0 0 H470 V34 C420 52 360 84 280 92 C190 100 110 86 0 96 Z" fill="var(--lime)"/>
      <path d="M0 0 H470 V28 C410 40 350 64 260 72 C170 80 90 66 0 76 Z" fill="var(--orange)"/>
    </svg>
    <p class="tagline tagline--banner">HollowReed Ideas<br>&amp; Hobby Materials</p>
    <h1 class="holder-name">Marit Olsson</h1>
    <ul class="contact-list">
      <li><span class="dot dot--orange"></span>+64 (0) 3 555 0142</li>
      <li><span class="dot dot--lime"></span>+64 (0) 21 555 01937</li>
      <li><span class="dot dot--grey"></span>marit.olsson@loomfield.example</li>
      <li><span class="dot dot--grey"></span>social.example/loomfield</li>
      <li><span class="dot dot--teal"></span>www.tindalerow.example</li>
      <li><span class="dot dot--orange"></span>www.loomfieldgoods.example</li>
    </ul>
    <div class="brand brand--front">
      <span class="brand__mark"></span>
      <span class="brand__name">Loomfield Goods Co.</span>
    </div>
  </section>

  <section class="card card--back" aria-label="Card back">
    <svg class="card__waves" viewBox="0 0 470 286" aria-hidden="true">
      <path d="M0 250 C90 222 180 222 260 250 C300 264 330 278 360 286 H0 Z" fill="var(--lime)"/>
      <path d="M0 262 C90 236 180 238 250 262 C280 272 300 280 330 286 H0 Z" fill="var(--orange)"/>
    </svg>
    <div class="brand brand--back">
      <span class="brand__mark"></span>
      <span class="brand__name">Loomfield Goods Co.</span>
    </div>
    <p class="tagline tagline--back">HollowReed Ideas &amp; Hobby Materials</p>
  </section>
</main>
</body>
</html>
```